Gymnastics Award Design Needed--for kids

Need a gymnastics certificate or award designed. Will be printed on a piece of 8.5x11 paper. The award will be celebrating the gymnast learning a new skill in gymnastics. So it should be fun, but still look "official". Needs to look good hanging on a gymnast's bedroom wall.

It should say "The Aerial Cartwheel Club"
I will be using this design to change it based on the skill.

My main colors are:
#34475D
#E1467A
#7555A4

So should use those, but can add others

My website is tumblenestpro.com so you can see the look/feel.

Target Market(s)

Main audience will be girls ages 5-12, but will also be used by slightly older girls and boys. So needs to be fun, not too gender specific.

Industry/Entity Type

Learning

Requirements
Must have
• The following will need to go on the certificate:
• * Name of Skill
• * Image of Skill
• * Gymnast's Name
• * my logo
• * Gym's Logo
• * Gym's Name
• Optional: Date

```html
<!DOCTYPE html>
<html lang="en">
<head>
<meta charset="utf-8">
<title>The Aerial Cartwheel Club – Skill Certificate</title>
<link rel="stylesheet" href="https://fonts.googleapis.com/css2?family=Pinyon+Script&family=Stardos+Stencil:wght@700&family=Josefin+Sans:wght@300;400&display=swap">
<style>
  :root {
    --paper: #ffffff;
    --surround: #eceafd;
    --frame-pink: #ee2ba8;
    --title-pink: #ef2aa9;
    --ink: #111111;
    --violet: #5a3ff0;
    --logo-violet: #6a4cf2;
    --muted: #222222;
  }
  * { margin: 0; padding: 0; box-sizing: border-box; }
  html, body { width: 1200px; height: 848px; overflow: hidden; background: var(--surround); }
  .certificate {
    position: relative;
    width: 1200px;
    height: 848px;
    background: var(--surround);
  }
  .frame {
    position: absolute;
    inset: 0;
  }
  .sheet {
    position: absolute;
    left: 26px; top: 26px; right: 26px; bottom: 26px;
    background: var(--paper);
  }
  .script { font-family: "Pinyon Script", cursive; font-weight: 400; color: var(--ink); }
  .heading-the {
    position: absolute; left: 0; right: 0; top: 28px;
    text-align: center; font-size: 78px; line-height: 1;
    -webkit-text-stroke: 1px var(--ink);
  }
  .club-title {
    position: absolute; left: 0; right: 0; top: 100px;
    text-align: center;
    font-family: "Stardos Stencil", fantasy;
    font-weight: 700;
    color: var(--title-pink);
    line-height: 0.98;
    text-transform: uppercase;
  }
  .club-title .line-one { display: block; font-size: 104px; letter-spacing: 2px; }
  .club-title .line-two { display: block; font-size: 104px; letter-spacing: 2px; }
  .skill-art {
    position: absolute; left: 80px; top: 334px; width: 424px; height: 136px;
    background: linear-gradient(180deg, #f7eef3 0%, #e9dcf5 55%, #d9c7f2 100%);
    border-bottom: 2px solid #b8bcc0;
  }
  .skill-name {
    position: absolute; left: 631px; top: 390px; width: 499px;
    text-align: center; font-size: 62px; line-height: 1;
    -webkit-text-stroke: 1px var(--ink);
  }
  .rule { position: absolute; height: 0; border-top: 2.5px solid var(--ink); }
  .rule-skill { left: 631px; top: 475px; width: 499px; }
  .presented {
    position: absolute; left: 138px; top: 512px;
    font-size: 60px; line-height: 1; color: var(--violet);
    -webkit-text-stroke: 1px var(--violet);
  }
  .rule-recipient { left: 527px; top: 564px; width: 534px; }
  .issuer {
    position: absolute; left: 0; right: 0; top: 590px;
    text-align: center; font-size: 62px; line-height: 1;
    -webkit-text-stroke: 1px var(--ink);
  }
  .date-label {
    position: absolute; left: 435px; top: 715px;
    font-size: 46px; line-height: 1;
    -webkit-text-stroke: 0.8px var(--ink);
  }
  .rule-date { left: 550px; top: 757px; width: 215px; }
  .gym-mark {
    position: absolute; left: 50px; top: 690px; width: 230px;
    text-align: center;
    font-family: "Josefin Sans", sans-serif; font-weight: 400;
    color: var(--muted);
  }
  .gym-mark .mark-shape {
    display: block; width: 46px; height: 46px; margin: 0 auto 14px;
    background: var(--violet); border-radius: 50%;
  }
  .gym-mark .mark-name { font-size: 28px; letter-spacing: 1px; }
  .brand-mark {
    position: absolute; left: 868px; top: 728px;
    display: flex; align-items: center; gap: 12px;
    font-family: "Josefin Sans", sans-serif; font-weight: 300;
    font-size: 31px; letter-spacing: 1px; text-transform: uppercase;
    color: var(--logo-violet);
  }
  .brand-mark .mark-shape {
    width: 30px; height: 30px; background: var(--logo-violet);
  }
</style>
</head>
<body>
<main class="certificate">
  <div class="sheet"></div>
  <svg class="frame" width="1200" height="848" viewBox="0 0 1200 848" aria-hidden="true">
    <g fill="none" stroke="var(--frame-pink)" stroke-width="8">
      <rect x="30" y="30" width="1140" height="788"/>
    </g>
    <g fill="var(--frame-pink)">
      <path d="M18 18 H128 V34 H34 V128 H18 Z"/>
      <path d="M1182 18 H1072 V34 H1166 V128 H1182 Z"/>
      <path d="M18 830 H128 V814 H34 V720 H18 Z"/>
      <path d="M1182 830 H1072 V814 H1166 V720 H1182 Z"/>
    </g>
  </svg>

  <div class="script heading-the">The</div>
  <h1 class="club-title">
    <span class="line-one">Aerial Cartwheel</span>
    <span class="line-two">Club</span>
  </h1>

  <div class="skill-art" role="img" aria-label="Illustration of a gymnast performing an aerial cartwheel in five stages on a floor line"></div>

  <div class="script skill-name">Name of Skill</div>
  <div class="rule rule-skill"></div>

  <div class="script presented">Presented To:</div>
  <div class="rule rule-recipient"></div>

  <div class="script issuer">by Harbor Lane Gymnastics Gym.</div>

  <div class="gym-mark">
    <span class="mark-shape"></span>
    <span class="mark-name">Harbor Lane Gym</span>
  </div>

  <div class="script date-label">Date:</div>
  <div class="rule rule-date"></div>

  <div class="brand-mark">
    <span class="mark-shape"></span>
    <span class="mark-name">Tumblenest Pro</span>
  </div>
</main>
</body>
</html>
```